Wine Label: Corvinte

The project is to create 3 wine labels. The brand name is "Corvinte"

What we need is to have 3 versions: red wine, white wine and rose.

The wine is for young and modern people, between 21 and 31 years old, so it need to be casual, modern and fun, but at the same time it needs to keep the Premiums of a good European wine.

It is from Italy.

Target Market(s)

Young adults, between 21 and 31 years old. wine lovers

Requirements
Must have
• - Modern colors (Black, silver, red, etc.)
• - Clean label
• - Clear font
• - Style
• - The brand + the type of wine (red, white or rose)
Nice to have
• - A symbol to represent the brand
Should not have
• - Many elements
• - No clear fonts
• - No funny colors

```html
<!DOCTYPE html>
<html lang="en">
<head>
<meta charset="UTF-8">
<title>Corvinte Red – Wine Label</title>
<link rel="stylesheet" href="https://fonts.googleapis.com/css2?family=Arimo:wght@700&display=swap">
<style>
  :root {
    --canvas: #fdfdfd;
    --flag-green: #008a00;
    --flag-white: #ffffff;
    --flag-red: #ff0000;
    --silver-top: #b3b3b3;
    --silver-bottom: #fdfdfd;
    --bar-dark: #3a3a3a;
    --bar-light: #8a8a8a;
    --wine-red: #a80000;
    --crowd-light: #8c8c8c;
    --crowd-dark: #000000;
  }
  * { margin: 0; padding: 0; box-sizing: border-box; }
  html, body {
    width: 1200px;
    height: 1000px;
    overflow: hidden;
    background: var(--canvas);
  }
  .canvas {
    position: relative;
    width: 1200px;
    height: 1000px;
  }
  .label {
    position: absolute;
    left: 476px;
    top: 253px;
    width: 239px;
    height: 454px;
    border-radius: 20px;
    overflow: hidden;
    background: var(--silver-bottom);
    font-family: "Arimo", Arial, sans-serif;
  }
  .flag-strip {
    position: absolute;
    top: 0; left: 0;
    width: 100%;
    height: 6px;
    display: flex;
  }
  .flag-strip span:nth-child(1) { flex: 84; background: var(--flag-green); }
  .flag-strip span:nth-child(2) { flex: 70; background: var(--flag-white); }
  .flag-strip span:nth-child(3) { flex: 85; background: var(--flag-red); }
  .silver-field {
    position: absolute;
    top: 6px; left: 0;
    width: 100%;
    height: 212px;
    background: linear-gradient(to bottom, var(--silver-top), #e4e4e4 80%, var(--silver-bottom));
  }
  .brand-banner {
    position: absolute;
    top: 171px;
    left: 0;
    width: 100%;
    height: 55px;
  }
  .banner-bar {
    position: absolute;
    left: 12px;
    width: 214px;
    height: 7px;
    background: linear-gradient(100deg, var(--bar-dark) 0%, var(--bar-dark) 45%, var(--bar-light) 60%, #6a6a6a 100%);
  }
  .banner-bar.top { top: 0; }
  .banner-bar.bottom { bottom: 0; }
  .banner-field {
    position: absolute;
    left: 10px;
    top: 7px;
    width: 219px;
    height: 41px;
    background: #ffffff;
  }
  .banner-tabs {
    position: absolute;
    top: 13px;
    width: 9px;
    display: flex;
    flex-direction: column;
    gap: 5px;
  }
  .banner-tabs.left { left: 2px; }
  .banner-tabs.right { right: 2px; }
  .banner-tabs span {
    height: 7px;
    border-radius: 3px;
    background: #4a4a4a;
  }
  .brand-name {
    position: absolute;
    left: 0;
    top: 7px;
    width: 100%;
    height: 41px;
    line-height: 41px;
    text-align: center;
    font-size: 34px;
    font-weight: 700;
    color: var(--wine-red);
    letter-spacing: 0.5px;
  }
  .wine-type {
    position: absolute;
    top: 231px;
    width: 100%;
    text-align: center;
    font-size: 22px;
    font-weight: 700;
    color: var(--wine-red);
  }
  .crowd-scene {
    position: absolute;
    left: 0;
    top: 348px;
    width: 100%;
    height: 106px;
    background: linear-gradient(to bottom, var(--crowd-light) 0%, #555 30%, var(--crowd-dark) 65%);
  }
  .vintage {
    position: absolute;
    top: 434px;
    width: 100%;
    text-align: center;
    font-size: 16px;
    font-weight: 700;
    letter-spacing: 4px;
    color: var(--wine-red);
  }
</style>
</head>
<body>
  <div class="canvas">
    <div class="label">
      <div class="flag-strip"><span></span><span></span><span></span></div>
      <div class="silver-field"></div>

      <div class="brand-banner">
        <div class="banner-bar top"></div>
        <div class="banner-tabs left"><span></span><span></span><span></span></div>
        <div class="banner-field"></div>
        <div class="banner-tabs right"><span></span><span></span><span></span></div>
        <div class="brand-name">CORVINTE</div>
        <div class="banner-bar bottom"></div>
      </div>

      <div class="wine-type">RED</div>

      <div class="crowd-scene" role="img" aria-label="Silhouette of a cheering concert crowd with raised hands"></div>
      <div class="vintage">2014</div>
    </div>
  </div>
</body>
</html>
```